Carpet cleaning company wants business card

Need an exciting new fresh design for business cards for my carpet cleaning /pest control business
www.tidewellhomecare.com.au
Can design include a lined section for quoting or information? Thanks !

```html
<!DOCTYPE html>
<html lang="en">
<head>
<meta charset="utf-8">
<title>Tidewell Home Care – Business Card</title>
<link href="https://fonts.googleapis.com/css2?family=Arimo:wght@400;700&display=swap" rel="stylesheet">
<style>
  :root {
    --bg: #cfd2d3;
    --paper: #fbfbfb;
    --brand-red: #d8262d;
    --brand-blue: #163f95;
    --ink: #3a3a3a;
    --rule: #e0484d;
  }
  * { box-sizing: border-box; margin: 0; padding: 0; }
  html, body { width: 1200px; height: 829px; overflow: hidden; }
  body {
    background: var(--bg);
    font-family: "Arimo", Arial, sans-serif;
    color: var(--ink);
    display: flex;
    align-items: center;
    justify-content: center;
    gap: 40px;
  }
  .card {
    position: relative;
    width: 540px;
    height: 310px;
    background: var(--paper);
    border-bottom: 5px solid var(--brand-blue);
    box-shadow: 0 14px 30px rgba(0,0,0,0.18);
  }
  .brand {
    display: flex;
    align-items: center;
    gap: 10px;
    font-weight: 700;
    color: var(--brand-blue);
    letter-spacing: -0.5px;
  }
  .brand-mark { background: var(--brand-red); flex: none; }
  .card-front .brand { position: absolute; left: 40px; top: 42px; font-size: 28px; }
  .card-front .brand-mark { width: 18px; height: 18px; }
  .rule {
    position: absolute;
    left: 40px; right: 40px; top: 150px;
    height: 1px;
    background: var(--rule);
  }
  .person {
    position: absolute;
    right: 40px; top: 96px;
    text-align: right;
  }
  .person-name { font-size: 24px; font-weight: 700; text-transform: uppercase; letter-spacing: 0.5px; }
  .person-name .first { color: var(--brand-red); }
  .person-name .last { color: var(--brand-blue); }
  .person-role { font-size: 15px; margin-top: 2px; }
  .contacts {
    position: absolute;
    left: 40px; top: 170px;
    list-style: none;
    font-size: 14px;
    line-height: 21px;
  }
  .contacts li { display: flex; align-items: center; gap: 7px; }
  .contacts svg { width: 11px; height: 11px; fill: var(--brand-blue); flex: none; }
  .address {
    position: absolute;
    right: 40px; bottom: 30px;
    text-align: right;
    font-size: 14px;
    line-height: 20px;
    font-style: normal;
  }
  .card-back { display: flex; align-items: center; justify-content: center; }
  .card-back .brand { font-size: 42px; }
  .card-back .brand-mark { width: 26px; height: 26px; }
</style>
</head>
<body>
  <section class="card card-front" aria-label="Business card front">
    <div class="brand"><span class="brand-mark"></span>Tidewell Home Care</div>
    <div class="person">
      <p class="person-name"><span class="first">Dana</span> <span class="last">Whitlow</span></p>
      <p class="person-role">Owner/CEO</p>
    </div>
    <div class="rule"></div>
    <ul class="contacts">
      <li><svg viewBox="0 0 12 12"><path d="M2.5 1 4.5 1 5.3 3.6 4 4.6C4.6 6 6 7.4 7.4 8L8.4 6.7 11 7.5 11 9.5C11 10.3 10.3 11 9.5 11 5 11 1 7 1 2.5 1 1.7 1.7 1 2.5 1Z"/></svg>07 5521 8640</li>
      <li><svg viewBox="0 0 12 12"><path d="M3.5 0.5h5a1 1 0 0 1 1 1v9a1 1 0 0 1-1 1h-5a1 1 0 0 1-1-1v-9a1 1 0 0 1 1-1Zm0.6 1.5v6.5h3.8V2Z"/></svg>0432 617 205</li>
      <li><svg viewBox="0 0 12 12"><path d="M0.5 2.5h11v7h-11Zm1 1 4.5 3.2 4.5-3.2Z"/></svg>hello@tidewellhomecare.com.au</li>
      <li><svg viewBox="0 0 12 12"><circle cx="6" cy="6" r="5.5"/></svg>www.tidewellhomecare.com.au</li>
    </ul>
    <address class="address">27 Harbour View Rd<br>Lindale Park, 4122</address>
  </section>

  <section class="card card-back" aria-label="Business card back">
    <div class="brand"><span class="brand-mark"></span>Tidewell Home Care</div>
  </section>
</body>
</html>
```